Fertilizer Company exhibiting products for sale at Fiber Trade Fair

Organic fertilizer company exhibiting at a hemp trade show. We have a 10x10 booth. There is no pipe and drape, so we are looking to have a fully custom canopy designed and printed with a backdrop and sides. Please submit designs as if I was looking at a full expo show display - Canopy, backdrop, side walls, tables, etc.

Target Market(s)

Hemp Businesses

Industry/Entity Type

Agriculture, Hemp, Fertilizer

Font styles to use
Sans Serif

Colors
0054AA
0677BA
7BADD7
CADEEF
E8F1F8
0094D4
00A9DD
6FCCEA
C7EBF8
E9F6FB
00AB8E
00BBA5
67D7C9
C6EFE9
E9F9F6
59FF00
82FF00
B8FF75
E3FFCB
F4FFEA
FFF300
FFF600
FEFA6F
FFFEC7
FFFEE8
FFC000
F8CF3A
FAE287
FDF2CF
FEFAEE
F0912C
F2A743
F7CA91
FBE8D2
FDF5EE
EE7325
F08F49
F5BC92
FAE3D3
FDF4ED

Requirements
Must have
• Custom designed canopy that integrates my branding files - Sky & Lightning Bolts, Pell Grove Logo
Should not have
• Red anywhere. Red in agriculture means dead.

```html
<!DOCTYPE html>
<html lang="en">
<head>
<meta charset="utf-8">
<title>Pell Grove – Booth Canopy Artwork</title>
<link href="https://fonts.googleapis.com/css2?family=Cabin+Condensed:wght@500;600&family=Oswald:wght@300&display=swap" rel="stylesheet">
<style>
  :root {
    --stage: #9ea9ba;
    --ink: #0d0d0d;
    --charcoal: #2e2e2e;
    --slate: #4a4a4a;
    --leaf: #a6ce39;
    --bright-leaf: #82ff00;
    --white: #ffffff;
    --sky-a: #0677ba;
    --sky-b: #0094d4;
    --bark: #5a4632;
  }
  * { box-sizing: border-box; margin: 0; padding: 0; }
  html, body { width: 1200px; height: 902px; overflow: hidden; }
  body {
    background: var(--stage);
    position: relative;
    font-family: "Cabin Condensed", sans-serif;
  }
  .panel { position: absolute; }

  /* roof panels */
  .roof { top: 24px; width: 560px; height: 150px; }
  .roof--left { left: 34px; }
  .roof--right { left: 606px; }
  .roof svg { position: absolute; inset: 0; }
  .roof__brand {
    position: absolute; left: 0; right: 0; top: 92px;
    text-align: center; color: var(--leaf);
    font-weight: 600; font-size: 26px; letter-spacing: 1px;
  }
  .roof__art {
    position: absolute; left: 210px; top: 52px; width: 140px; height: 60px;
    border-radius: 50% 50% 8px 8px;
    background: radial-gradient(ellipse at 50% 40%, var(--leaf), #3d5a1a 60%, var(--sky-a));
  }
  .roof__product {
    position: absolute; left: 0; right: 0; top: 112px;
    text-align: center; color: var(--white);
    font-weight: 600; font-size: 26px; letter-spacing: 2px;
  }

  /* valance */
  .valance {
    top: 186px; width: 560px; height: 84px;
    background: var(--ink);
    display: flex; align-items: center; justify-content: center;
    color: var(--white);
    font-family: "Oswald", sans-serif; font-weight: 300;
    font-size: 50px; letter-spacing: 1px;
  }
  .valance--left { left: 34px; }
  .valance--right { left: 606px; }

  /* backdrop */
  .backdrop {
    left: 340px; top: 290px; width: 520px; height: 270px;
    background: linear-gradient(180deg, #555 0%, var(--charcoal) 100%);
    overflow: hidden;
  }
  .backdrop svg { position: absolute; left: 0; bottom: 0; }
  .backdrop__brand {
    position: absolute; top: 58px; left: 0; right: 0;
    display: flex; align-items: center; justify-content: center; gap: 18px;
  }
  .backdrop__mark {
    width: 54px; height: 54px; border-radius: 50%;
    background: var(--leaf);
  }
  .backdrop__name {
    color: var(--white); font-weight: 600; font-size: 66px; line-height: 1;
  }

  /* half walls */
  .wall {
    top: 590px; width: 560px; height: 280px;
    background: var(--ink); overflow: hidden;
  }
  .wall--left { left: 34px; }
  .wall--right { left: 606px; }
  .wall svg.wall__split { position: absolute; inset: 0; }
  .wall__benefits {
    position: absolute; left: 22px; top: 62px;
    list-style: none; color: var(--ink);
    font-weight: 600; font-size: 29px; line-height: 1.28;
  }
  .wall__benefits li { padding-left: 18px; position: relative; }
  .wall__benefits li::before {
    content: ""; position: absolute; left: 0; top: 16px;
    width: 6px; height: 6px; border-radius: 50%; background: var(--ink);
  }
  .wall__benefits .cont::before { display: none; }
  .wall__art {
    position: absolute; left: 300px; top: 24px; width: 200px; height: 150px;
    border-radius: 50% 50% 10px 10px;
    background: radial-gradient(ellipse at 50% 45%, var(--leaf) 0%, #3c5b1c 45%, var(--sky-a) 75%, var(--ink) 100%);
  }
  .wall__product {
    position: absolute; left: 240px; width: 300px; top: 160px;
    text-align: center; color: var(--white);
    font-weight: 600; font-size: 56px; line-height: 1;
  }
  .wall__tagline {
    position: absolute; left: 250px; width: 280px; top: 222px;
    background: var(--slate); color: #ddd;
    font-weight: 500; font-size: 14px; text-align: center; padding: 4px 0;
  }
</style>
</head>
<body>

  <section class="panel roof roof--left">
    <svg width="560" height="150" viewBox="0 0 560 150"><polygon points="280,0 560,150 0,150" fill="#2e2e2e"/></svg>
    <div class="roof__brand">Pell Grove</div>
  </section>

  <section class="panel roof roof--right">
    <svg width="560" height="150" viewBox="0 0 560 150"><polygon points="280,0 560,150 0,150" fill="#2e2e2e"/></svg>
    <div class="roof__art" role="img" aria-label="Tree with green leaves against a stormy sky with lightning bolts"></div>
    <div class="roof__product">Root Surge</div>
  </section>

  <div class="panel valance valance--left">ORGANIC FERTILIZER</div>
  <div class="panel valance valance--right">ORGANIC FERTILIZER</div>

  <section class="panel backdrop">
    <div class="backdrop__brand">
      <span class="backdrop__mark"></span>
      <span class="backdrop__name">Pell Grove</span>
    </div>
    <svg width="520" height="90" viewBox="0 0 520 90">
      <path d="M0 30 Q260 110 520 10 V90 H0 Z" fill="#141414"/>
      <path d="M0 30 Q260 110 520 10" fill="none" stroke="#ffffff" stroke-width="8"/>
      <path d="M0 22 Q260 100 520 2" fill="none" stroke="#a6ce39" stroke-width="6"/>
    </svg>
  </section>

  <section class="panel wall wall--left">
    <svg class="wall__split" width="560" height="280" viewBox="0 0 560 280">
      <path d="M0 0 H190 Q228 140 200 280 H0 Z" fill="#a6ce39"/>
      <path d="M190 0 Q228 140 200 280" fill="none" stroke="#ffffff" stroke-width="4"/>
    </svg>
    <ul class="wall__benefits">
      <li>Fast Growth</li>
      <li>Vigorous Roots</li>
      <li>Performance</li>
      <li class="cont">boost</li>
    </ul>
    <div class="wall__art" role="img" aria-label="Tree with green leaves surrounded by blue lightning bolts"></div>
    <div class="wall__product">Root Surge</div>
    <div class="wall__tagline">fast growth | vigorous roots | performance boost</div>
  </section>

  <section class="panel wall wall--right">
    <svg class="wall__split" width="560" height="280" viewBox="0 0 560 280">
      <path d="M0 0 H190 Q228 140 200 280 H0 Z" fill="#a6ce39"/>
      <path d="M190 0 Q228 140 200 280" fill="none" stroke="#ffffff" stroke-width="4"/>
    </svg>
    <ul class="wall__benefits">
      <li>Fast Growth</li>
      <li>Vigorous Roots</li>
      <li>Performance</li>
      <li class="cont">boost</li>
    </ul>
    <div class="wall__art" role="img" aria-label="Tree with green leaves surrounded by blue lightning bolts"></div>
    <div class="wall__product">Root Surge</div>
    <div class="wall__tagline">fast growth | vigorous roots | performance boost</div>
  </section>

</body>
</html>
```